Events By Halvane

Weddings, Corporate, Special Events
Memorable Catering, Personalized Menus, Custom Layout & Designs
Professional Staff, Excellent Service
Our Mission is Turning YOUR Vision into a Reality

Odette Halvane, Principal Planner
ph. 202 418-7352 - fax 301-847-2951
Email - eventsbyhalvane@mailtrove.com
Web - www.cateringbyhalvane.com
cateringbyhalvane@Instagram

Target Market(s)

All Brides, Corprate Business, Special Events

Industry/Entity Type

Hospitality

Contact Information for Business Card

clean but affective

Font styles to use
Serif
Sans Serif
Script

Colors

Designer to choose colors to be used in the design.

Requirements
Must have
• logo with tagline using colors that will enhance what
• some pictures of nice table scape, hors d'oevures, upscale foods......
Nice to have
• Event: Something that happens or is regarded as happening, an occurrence especially one of some importance.
Should not have
• Use Logo on both sides

```html
<!DOCTYPE html>
<html lang="en">
<head>
<meta charset="utf-8">
<title>Events By Halvane – Business Card</title>
<link rel="stylesheet" href="https://fonts.googleapis.com/css2?family=Libre+Baskerville:ital@0;1&display=swap">
<style>
  :root {
    --paper: #ffffff;
    --ink-grey: #8e8e8e;
    --ink-divider: #555555;
    --accent-gold: #b9a14c;
    --wood-light: #6a4530;
    --wood-mid: #4a2e1f;
    --wood-dark: #2c1a11;
  }
  * { margin: 0; padding: 0; box-sizing: border-box; }
  html, body { width: 1200px; height: 1000px; overflow: hidden; background: var(--paper); }
  .card {
    position: relative;
    width: 1200px;
    height: 1000px;
    background: var(--paper);
    font-family: "Libre Baskerville", Georgia, serif;
    color: var(--ink-grey);
  }
  .services {
    position: absolute;
    left: 52px;
    top: 206px;
    font-size: 26px;
    line-height: 43px;
    text-transform: uppercase;
    list-style: none;
  }
  .offer {
    position: absolute;
    left: 52px;
    top: 336px;
    font-style: italic;
    font-size: 26px;
    line-height: 44px;
    letter-spacing: 1.6px;
  }
  .contact {
    position: absolute;
    left: 52px;
    top: 458px;
    font-size: 26px;
    line-height: 43px;
    font-style: normal;
  }
  .contact .divider { color: var(--ink-divider); padding: 0 4px; }
  .social {
    position: absolute;
    left: 62px;
    top: 646px;
    display: flex;
    gap: 18px;
  }
  .social span {
    width: 30px;
    height: 30px;
    border-radius: 50%;
    background: var(--ink-grey);
  }
  .mission {
    position: absolute;
    left: 52px;
    top: 725px;
    font-style: italic;
    font-size: 27px;
    line-height: 39px;
    letter-spacing: 1px;
    color: var(--accent-gold);
  }
  .food-photo {
    position: absolute;
    left: 624px;
    top: 157px;
    width: 576px;
    height: 685px;
    background: linear-gradient(135deg, var(--wood-light) 0%, var(--wood-mid) 50%, var(--wood-dark) 100%);
  }
</style>
</head>
<body>
<main class="card">
  <ul class="services">
    <li>Weddings</li>
    <li>Corporate,</li>
    <li>Special Events</li>
  </ul>
  <p class="offer">Memorable Catering,<br>Personalized Menus and Designs</p>
  <address class="contact">
    Odette Halvane Principal Planner<br>
    c. 202 418-7352 <span class="divider">|</span> f. 301-847-2951<br>
    www.eventsbyhalvane.com<br>
    cateringbyhalvane@mailtrove.com
  </address>
  <div class="social" aria-label="Social media links">
    <span></span><span></span><span></span>
  </div>
  <p class="mission">Our Mission is Turning<br>-Your- Vision into a Reality</p>
  <div class="food-photo" role="img" aria-label="Photo of plated meringue desserts on lemon curd and chocolate truffles on white dishes over a dark wooden table with a copper centerpiece"></div>
</main>
</body>
</html>
```